Anchored Willow Website

Would like a website designed for my fitness and nutrition coaching company Anchor Willow. I have a company logo and would like to keep the page layout clean and simple. Needs to look great on computer and mobile devices.

Target Market(s)

Target market is individuals looking to make changes in their health and nutrition with the help of an online coach.

Industry/Entity Type

Fitness

Number of Pages Required

2 page

Colors
3176b5
0355a3
85acd3
cedeed
f8fcfd
ffffff

Requirements
Must have
• The first page should have the company logo and name towards the top and below that client before and after photos scrolling or displaying in some manner. Also would like a section that states services offered and a section about myself since I am the primary coach for clients.

```html
<!DOCTYPE html>
<html lang="en">
<head>
<meta charset="utf-8">
<title>Anchored Willow — Fitness Company</title>
<link href="https://fonts.googleapis.com/css2?family=Roboto:ital,wght@0,300;0,400;0,500;0,700;0,900;1,500;1,700&display=swap" rel="stylesheet">
<style>
:root{
  --blue:#3176b5;
  --deep:#0355a3;
  --sky:#85acd3;
  --mist:#cedeed;
  --paper:#f8fcfd;
  --white:#ffffff;
  --page:#f0f5f9;
  --navy:#062a52;
  --navy-2:#041f3e;
  --ink:#5b6470;
  --ink-dark:#2a3340;
}
*{box-sizing:border-box;margin:0;padding:0}
html,body{width:1200px;height:2956px;overflow:hidden}
body{font-family:"Roboto",Arial,sans-serif;background:var(--page);color:var(--ink);position:relative}
a{color:inherit;text-decoration:none}
ul{list-style:none}

/* Header */
.site-header{position:absolute;top:0;left:0;width:1200px;height:59px;background:var(--paper);border-bottom:1px solid var(--mist)}
.brand{position:absolute;left:234px;top:10px;display:flex;flex-direction:column;align-items:center;gap:4px}
.brand-mark{width:22px;height:22px;background:var(--blue)}
.brand-name{font-size:10px;font-weight:700;color:var(--blue);letter-spacing:.5px;text-transform:uppercase;white-space:nowrap}
.main-nav{position:absolute;left:478px;top:0;width:392px;height:59px;display:flex;align-items:center;justify-content:space-between;font-size:9px;font-weight:700;letter-spacing:.4px;color:var(--ink-dark);white-space:nowrap}
.main-nav .active{color:var(--blue)}
.header-social{position:absolute;left:892px;top:0;width:74px;height:59px;display:flex;gap:10px;align-items:center;justify-content:center;border-left:1px solid var(--mist);border-right:1px solid var(--mist)}
.header-social span{width:7px;height:7px;border-radius:50%;background:var(--blue)}

/* Hero */
.hero{position:absolute;top:59px;left:0;width:1200px;height:461px;background:linear-gradient(120deg,#0c4f95 0%,#1d64ad 45%,#2b6bb0 70%,#1c5699 100%);overflow:hidden}
.hero-photo{position:absolute;left:590px;top:0;width:400px;height:461px;background:radial-gradient(ellipse at 50% 55%,#3a78b8 0%,#2262a6 55%,rgba(29,96,168,0) 80%)}
.hero-frame{position:absolute;left:632px;top:107px;width:259px;height:259px;border:5px solid var(--white);transform:rotate(45deg)}
.hero-copy{position:absolute;left:234px;top:128px}
.hero-title{font-size:35px;font-weight:900;color:#2f82d6;letter-spacing:.5px;line-height:1}
.hero-sub{font-size:19px;font-weight:300;color:var(--white);letter-spacing:3px;margin-top:2px}
.hero-text{font-size:12px;color:#8ab4e0;line-height:18px;margin-top:18px;width:330px}
.btn{display:inline-flex;align-items:center;justify-content:center;border-radius:17px;font-size:10px;font-weight:500;letter-spacing:.6px;text-transform:uppercase;color:var(--white)}
.hero .btn{position:absolute;left:234px;top:298px;width:120px;height:32px;background:var(--blue)}

/* Services */
.services{position:absolute;top:520px;left:0;width:1200px;height:225px;display:flex}
.service{width:400px;padding:58px 0 0 87px;color:var(--white)}
.service:nth-child(1){background:var(--deep)}
.service:nth-child(2){background:var(--blue)}
.service:nth-child(3){background:var(--sky)}
.service h3{font-size:14px;font-weight:700;letter-spacing:.3px}
.service p{font-size:10.5px;line-height:15px;margin-top:14px;width:230px;opacity:.92}
.more{display:inline-flex;align-items:center;gap:8px;font-size:8px;font-weight:700;font-style:italic;letter-spacing:.4px;margin-top:22px;text-transform:uppercase}

/* About */
.about{position:absolute;top:745px;left:0;width:1200px;height:374px;background:var(--page)}
.about-copy{position:absolute;left:234px;top:58px;width:300px}
.about h2{font-size:19px;font-weight:700;color:var(--blue)}
.about p{font-size:10.5px;line-height:15px;color:#7c8591;margin-top:28px}
.about p + p{margin-top:12px}
.about .btn{position:absolute;left:234px;top:286px;width:120px;height:34px;background:var(--blue)}
.about-photo{position:absolute;left:600px;top:0;width:600px;height:374px;background:linear-gradient(135deg,#3c3f46 0%,#23262c 50%,#1a1c20 100%)}

/* Features */
.features{position:absolute;top:1119px;left:0;width:1200px;height:185px;background:linear-gradient(100deg,#6a6c71 0%,#5f6166 40%,#75777c 65%,#636569 100%)}
.feature{position:absolute;top:58px;width:200px;margin-left:-100px;text-align:center;color:var(--white)}
.feature svg{display:block;margin:0 auto}
.feature h4{font-size:10px;font-weight:700;letter-spacing:.3px;margin-top:11px;text-transform:uppercase}
.feature p{font-size:10px;line-height:14px;margin-top:8px;color:#e3e5ea}

/* Classes */
.classes{position:absolute;top:1304px;left:0;width:1200px;height:495px;background:var(--paper)}
.section-title{position:absolute;left:0;width:1200px;text-align:center;font-size:19px;font-weight:700;color:var(--blue);letter-spacing:.3px}
.classes .section-title{top:55px}
.class-card{position:absolute;top:110px;width:231px}
.class-photo{position:relative;height:168px}
.price{position:absolute;right:0;top:0;width:36px;height:36px;background:var(--blue);color:var(--white);font-size:11px;font-weight:700;display:flex;align-items:center;justify-content:center}
.class-card h3{font-size:10px;font-weight:700;color:var(--blue);margin-top:18px}
.class-card p{font-size:9.5px;line-height:14px;color:#8a929c;margin-top:7px}
.class-card .more{color:var(--ink-dark);margin-top:10px}
.pager{position:absolute;left:0;width:1200px;display:flex;justify-content:center;gap:8px}
.pager span{width:18px;height:18px;border:1px solid #b8c2cc;display:flex;align-items:center;justify-content:center}
.classes .pager{top:420px}

/* CTA */
.cta{position:absolute;top:1799px;left:0;width:1200px;height:124px;background:var(--deep);color:var(--white)}
.cta h2{position:absolute;left:234px;top:42px;font-size:14.5px;font-weight:700;letter-spacing:.3px}
.cta p{position:absolute;left:234px;top:68px;font-size:10.5px;color:#cfe0f2}
.cta .btn{position:absolute;left:847px;top:46px;width:119px;height:32px;border:1.5px solid var(--white)}

/* Before and after */
.results{position:absolute;top:1923px;left:0;width:1200px;height:437px;background:var(--page)}
.results .section-title{top:58px}
.result-row{position:absolute;top:114px;left:0;width:1200px;display:flex;gap:3px}
.result{width:298px;position:relative}
.result-photos{display:flex;height:181px}
.result-photos div{flex:1;position:relative}
.result-photos .before{background:linear-gradient(180deg,#c8d8ea,#b7c9de)}
.result-photos .after{background:linear-gradient(180deg,#d7e2ee,#c6d3e3)}
.result-photos.skin .before{background:linear-gradient(180deg,#d8b7a3,#b98d76)}
.result-photos.skin .after{background:linear-gradient(180deg,#c99a80,#9e6d55)}
.tag{position:absolute;bottom:0;right:0;font-size:9px;font-weight:700;font-style:italic;color:var(--white);background:rgba(49,118,181,.85);padding:3px 6px 3px 14px;clip-path:polygon(12px 0,100% 0,100% 100%,0 100%)}
.result-label{height:24px;background:var(--blue);color:var(--white);font-size:9.5px;display:flex;align-items:center;justify-content:center;gap:4px;letter-spacing:.2px}
.result-label b{font-weight:700;font-style:italic}
.results .pager{top:356px}

/* Testimonials */
.testimonials{position:absolute;top:2360px;left:0;width:1200px;height:309px;background:linear-gradient(115deg,#0a4a8d 0%,#1459a3 40%,#0c4a90 70%,#0b3f7c 100%)}
.testimonials .section-title{top:54px;color:var(--white)}
.quote{position:absolute;top:137px;width:300px;display:flex;gap:20px;color:var(--white)}
.avatar{flex:none;width:60px;height:60px;border-radius:50%;border:3px solid var(--white);background:linear-gradient(180deg,#e3b997,#c9926d)}
.quote h4{font-size:10px;font-weight:700;margin-top:6px}
.quote p{font-size:10px;line-height:14px;margin-top:9px;color:#d4e3f3}
.testimonials .pager{top:253px}
.testimonials .pager span{border-color:var(--white)}

/* Footer */
.site-footer{position:absolute;top:2669px;left:0;width:1200px;height:287px;background:linear-gradient(180deg,var(--navy),var(--navy-2));color:#b9c8da}
.footer-brand{position:absolute;left:234px;top:42px;width:160px}
.footer-brand .brand-mark{width:40px;height:40px;margin-left:40px}
.footer-brand .brand-name{display:block;text-align:center;font-size:12px;margin-top:10px;color:var(--blue)}
.footer-brand p{font-size:8.5px;line-height:12px;margin-top:10px;color:#8ea3bc}
.footer-col{position:absolute;top:46px}
.footer-col h5{font-size:10px;font-weight:700;color:var(--blue);letter-spacing:.4px;text-transform:uppercase}
.footer-links li{font-size:9px;color:var(--white);margin-top:23px;display:flex;align-items:center;gap:8px}
.footer-links li::before{content:"";width:3px;height:3px;border-radius:50%;background:var(--white)}
.post{margin-top:20px;width:190px}
.post p{font-size:9px;line-height:14px;color:var(--white)}
.post time{display:block;font-size:8.5px;color:var(--blue);margin-top:4px}
.post + .post{margin-top:24px}
.contact-list{margin-top:20px;font-size:9px}
.contact-list div{display:flex;margin-bottom:11px}
.contact-list dt{width:38px;color:var(--white);font-weight:500}
.contact-list dd{color:#b9c8da}
.footer-bottom{position:absolute;left:234px;top:258px;width:732px;display:flex;justify-content:space-between;font-size:8.5px;color:#8ea3bc}
.footer-bottom nav{display:flex;gap:12px;color:#b9c8da}
</style>
</head>
<body>

<header class="site-header">
  <a class="brand" href="#"><span class="brand-mark"></span><span class="brand-name">Anchored Willow</span></a>
  <nav class="main-nav">
    <a class="active" href="#">HOME</a><a href="#">NEWS</a><a href="#">CLASSES</a><a href="#">SCHEDULE</a><a href="#">TESTIMONIALS</a><a href="#">CONTACT</a>
  </nav>
  <div class="header-social"><span></span><span></span><span></span></div>
</header>

<section class="hero">
  <div class="hero-photo" role="img" aria-label="Athlete swinging kettlebells overhead, tinted blue"></div>
  <div class="hero-frame"></div>
  <div class="hero-copy">
    <h1 class="hero-title">ANCHORED WILLOW</h1>
    <p class="hero-sub">FITNESS COMPANY</p>
    <p class="hero-text">Curabitur laoreet ex turpis. Vestibulum sit amet liber augue, sit amet vehicula mi. Aliquam vitae varius.</p>
  </div>
  <a class="btn" href="#">Get started</a>
</section>

<section class="services">
  <article class="service">
    <h3>PERSONAL TRAINING</h3>
    <p>Quisque aliquam condimentum vulputate. Nulla facilisi. Sed tempor dolor egestas mi placerat fringilla. Sed cursus pharetra eros.</p>
    <a class="more" href="#">Learn more <svg width="10" height="6" viewBox="0 0 10 6"><path d="M0 3h9M6.5 .5 9 3 6.5 5.5" stroke="currentColor" fill="none"/></svg></a>
  </article>
  <article class="service">
    <h3>FITNESS</h3>
    <p>Quisque aliquam condimentum vulputate. Nulla facilisi. Sed tempor dolor egestas mi placerat fringilla. Sed cursus pharetra eros.</p>
    <a class="more" href="#">Learn more <svg width="10" height="6" viewBox="0 0 10 6"><path d="M0 3h9M6.5 .5 9 3 6.5 5.5" stroke="currentColor" fill="none"/></svg></a>
  </article>
  <article class="service">
    <h3>NUTRITIONS</h3>
    <p>Quisque aliquam condimentum vulputate. Nulla facilisi. Sed tempor dolor egestas mi placerat fringilla. Sed cursus pharetra eros.</p>
    <a class="more" href="#">Learn more <svg width="10" height="6" viewBox="0 0 10 6"><path d="M0 3h9M6.5 .5 9 3 6.5 5.5" stroke="currentColor" fill="none"/></svg></a>
  </article>
</section>

<section class="about">
  <div class="about-copy">
    <h2>ABOUT US</h2>
    <p>Donec ut nisi et nibh iaculis gravida. Nam a auctor libero. Etiam iosm et odio eget vulputate. Nulla ut ligula sed diam suscipit commentum eget sit amet quam. Ut vitae feugiat ipsum. Duis condim tum lectus quis blandit egestas. Sed euismod nisi ut ullamcorper consequat. Morbi vel malesuada dui.</p>
    <p>Phasellus ornare quam eget vestibulum rhoncus. Integer hendre tempor vehicula. Suspendisse orci nisi, sollicitudin vitae turpis, cursus pharetra urna.</p>
  </div>
  <a class="btn" href="#">More about us</a>
  <div class="about-photo" role="img" aria-label="Coach guiding a client through a suspension strap workout in a gym"></div>
</section>

<section class="features" role="img" aria-label="Dimmed gym background">
  <div class="feature" style="left:317px">
    <svg width="24" height="22" viewBox="0 0 24 22" fill="none" stroke="#fff" stroke-width="1.3"><path d="M4 13V10a8 8 0 0 1 16 0v3"/><rect x="2.5" y="12" width="4" height="7" rx="1.5"/><rect x="17.5" y="12" width="4" height="7" rx="1.5"/></svg>
    <h4>Free consultation</h4>
    <p>Donec finibus ulicies vulputate turpis,<br>id mollis massa laoreet</p>
  </div>
  <div class="feature" style="left:504px">
    <svg width="24" height="22" viewBox="0 0 24 22" fill="none" stroke="#fff" stroke-width="1.3"><path d="M12 1.5l3 6.4 7 .8-5.2 4.8 1.4 6.9L12 17l-6.2 3.4 1.4-6.9L2 8.7l7-.8z"/></svg>
    <h4>Excellent service</h4>
    <p>Aenean sagittis sodales tincidunt<br>augue ut sagittis faucibus</p>
  </div>
  <div class="feature" style="left:690px">
    <svg width="24" height="22" viewBox="0 0 24 22" fill="none" stroke="#fff" stroke-width="1.3"><path d="M7 2h10v6a5 5 0 0 1-10 0zM7 4H3a4 4 0 0 0 4 5M17 4h4a4 4 0 0 1-4 5M12 13v4M8 20h8"/></svg>
    <h4>Best trainers</h4>
    <p>Praesent non varius neque porta<br>egestas sem faucibus</p>
  </div>
  <div class="feature" style="left:896px">
    <svg width="24" height="22" viewBox="0 0 24 22" fill="none" stroke="#fff" stroke-width="1.3"><path d="M3 10h4v10H3zM7 10l4-8c2 0 3 1.5 2.5 3.5L13 9h6a2 2 0 0 1 2 2.4l-1.4 6.6A2.5 2.5 0 0 1 17 20H7"/></svg>
    <h4>Work programs</h4>
    <p>Curabitur ut suscipit nisi mattis elit,<br>magna libero velit</p>
  </div>
</section>

<section class="classes">
  <h2 class="section-title">OUR CLASSES</h2>
  <article class="class-card" style="left:234px">
    <div class="class-photo" role="img" aria-label="Two people sparring in a dark studio" style="background:linear-gradient(135deg,#2c3038,#15171b)"><span class="price">$50</span></div>
    <h3>PERSONAL TRAINER</h3>
    <p>Suspendisse vel nisl sed turpis viverra tincidunt. Vivamus et lobortis felis. Proin accumsan orci eu quam facilisis, et egestas.</p>
    <a class="more" href="#">Learn more <svg width="10" height="6" viewBox="0 0 10 6"><path d="M0 3h9M6.5 .5 9 3 6.5 5.5" stroke="currentColor" fill="none"/></svg></a>
  </article>
  <article class="class-card" style="left:485px">
    <div class="class-photo" role="img" aria-label="Group training class exercising in a bright gym" style="background:linear-gradient(135deg,#8a9aa5,#5e6d76)"><span class="price">$35</span></div>
    <h3>GROUP TRAINING</h3>
    <p>Proin rutrum lectus leo, lobortis sollicitudin turpis eleifend et. Sed sit amet mauris vel orci pretium faucibus eget vitae nisl.</p>
    <a class="more" href="#">Learn more <svg width="10" height="6" viewBox="0 0 10 6"><path d="M0 3h9M6.5 .5 9 3 6.5 5.5" stroke="currentColor" fill="none"/></svg></a>
  </article>
  <article class="class-card" style="left:735px">
    <div class="class-photo" role="img" aria-label="Athlete doing dumbbell push-ups on a dark floor" style="background:linear-gradient(135deg,#4a4d52,#232427)"><span class="price">$45</span></div>
    <h3>WORKOUT</h3>
    <p>Vestibulum malesuada ligula justo, in efficitur sap ien bibendum sed. Sed efficitur sit amet augue quis posuere.</p>
    <a class="more" href="#">Learn more <svg width="10" height="6" viewBox="0 0 10 6"><path d="M0 3h9M6.5 .5 9 3 6.5 5.5" stroke="currentColor" fill="none"/></svg></a>
  </article>
  <div class="pager">
    <span><svg width="5" height="8" viewBox="0 0 5 8"><path d="M4 1 1 4l3 3" stroke="#7c8591" fill="none"/></svg></span>
    <span><svg width="5" height="8" viewBox="0 0 5 8"><path d="M1 1l3 3-3 3" stroke="#7c8591" fill="none"/></svg></span>
  </div>
</section>

<section class="cta">
  <h2>GOT A QUESTIONS? WANT TO WORK WITH US?</h2>
  <p>Pellentesque sed nibh blandit, ultricies eros at, dignissim tellus ac eleifend velit.</p>
  <a class="btn" href="#">Contact us</a>
</section>

<section class="results">
  <h2 class="section-title">BEFORE AND AFTER</h2>
  <div class="result-row">
    <figure class="result">
      <div class="result-photos skin">
        <div class="before" role="img" aria-label="Client torso before the program"><span class="tag">Before</span></div>
        <div class="after" role="img" aria-label="Client torso after the program"><span class="tag">After</span></div>
      </div>
      <figcaption class="result-label"><b>4 MONTHS</b> OF WEIGHT STABILITY</figcaption>
    </figure>
    <figure class="result">
      <div class="result-photos">
        <div class="before" role="img" aria-label="Client full body before the program"><span class="tag">Before</span></div>
        <div class="after" role="img" aria-label="Client full body after the program"><span class="tag">After</span></div>
      </div>
      <figcaption class="result-label"><b>10 MONTHS</b> OF WEIGHT STABILITY</figcaption>
    </figure>
    <figure class="result">
      <div class="result-photos skin">
        <div class="before" role="img" aria-label="Client torso before the program"><span class="tag">Before</span></div>
        <div class="after" role="img" aria-label="Client torso after the program"><span class="tag">After</span></div>
      </div>
      <figcaption class="result-label"><b>4 MONTHS</b> OF WEIGHT STABILITY</figcaption>
    </figure>
    <figure class="result">
      <div class="result-photos">
        <div class="before" role="img" aria-label="Client full body before the program"><span class="tag">Before</span></div>
        <div class="after" role="img" aria-label="Client full body after the program"><span class="tag">After</span></div>
      </div>
      <figcaption class="result-label"><b>10 MONTHS</b> OF WEIGHT STABILITY</figcaption>
    </figure>
  </div>
  <div class="pager">
    <span><svg width="5" height="8" viewBox="0 0 5 8"><path d="M4 1 1 4l3 3" stroke="#7c8591" fill="none"/></svg></span>
    <span><svg width="5" height="8" viewBox="0 0 5 8"><path d="M1 1l3 3-3 3" stroke="#7c8591" fill="none"/></svg></span>
  </div>
</section>

<section class="testimonials">
  <h2 class="section-title">TESTIMONIALS</h2>
  <blockquote class="quote" style="left:234px">
    <div class="avatar" role="img" aria-label="Client portrait"></div>
    <div><h4>MARINA K.</h4><p>Maecenas auctor nibh elit, facilisis hendrerit libero susci pit a. Integer eget pharetra nulla. Etiam eget sollicitu din libero molestie.</p></div>
  </blockquote>
  <blockquote class="quote" style="left:610px">
    <div class="avatar" role="img" aria-label="Client portrait"></div>
    <div><h4>MARINA K.</h4><p>Vestibulum at mattis nibh. Proin in sapien sed lacus ultrices fringilla. Sed nunc augue ac quam ullamcorper lacinia eu vitae sem.</p></div>
  </blockquote>
  <div class="pager">
    <span><svg width="5" height="8" viewBox="0 0 5 8"><path d="M4 1 1 4l3 3" stroke="#fff" fill="none"/></svg></span>
    <span><svg width="5" height="8" viewBox="0 0 5 8"><path d="M1 1l3 3-3 3" stroke="#fff" fill="none"/></svg></span>
  </div>
</section>

<footer class="site-footer">
  <div class="footer-brand">
    <span class="brand-mark" style="display:block"></span>
    <span class="brand-name">Anchored Willow</span>
    <p>In hac habitasse platea dictumst. Curabitur ut neque metus. Vivamus sit amet dapibus odio, id laoreet elit. Suspendisse sit amet pharetra diam. Interdum et malesuada fames ac ante ipsum primis in faucibus.</p>
  </div>
  <div class="footer-col" style="left:404px">
    <h5>Company</h5>
    <ul class="footer-links"><li>About Us</li><li>Classes</li><li>Testimonials</li><li>Contact Us</li></ul>
  </div>
  <div class="footer-col" style="left:605px">
    <h5>From the blog</h5>
    <div class="post"><p>Ne magna libendum.Pellentesque vel viverra odio, fermentum.</p><time>22 September 2017</time></div>
    <div class="post"><p>Ne magna libendum.Pellentesque vel viverra odio, fermentum.</p><time>14 September 2017</time></div>
  </div>
  <div class="footer-col" style="left:802px">
    <h5>Contact us</h5>
    <dl class="contact-list">
      <div><dt>Phone</dt><dd>0 555 210 734</dd></div>
      <div><dt>Mail</dt><dd>hello@anchoredwillow.fit</dd></div>
      <div><dt>Adress</dt><dd>Harbor Lane 14, Portview</dd></div>
    </dl>
  </div>
  <div class="footer-bottom">
    <span>Copyright © 2017 Anchored Willow. All rights reserved.</span>
    <nav><a href="#">Community</a><span>|</span><a href="#">Updates</a><span>|</span><a href="#">Gallery</a></nav>
  </div>
</footer>

</body>
</html>
```